FACEBOOK PAGE FOR QUILLON PLUMBING GROUP

We need a facebook banner for our new plumbing business.

Needs to be catchy and inline with our logo.

Phone: 0491 726 384
Email: hello@quillon.com.au
website: www.quillon.com.au
Servicing: Perth Metro Areas and surrounding suburbs
Services:
*We offer a wide range of services, including:
Plumbing – General maintenance, blocked drains, toilet repairs, burst pipes, reticulation, renovations & emergencies.

*Hot Water – Installation, servicing & repairs for all systems.

*Cooling & Heating – Air conditioning, evaporative cooling & heater servicing.

*Filtration – Filtered taps, under-sink systems & whole-house filtration setups.

Our Mission

Quillon Group believes plumbing shouldn't break the bank - or your trust. Our mission is to provide honest, affordable, and no-nonsense plumbing services that get the job done right the first time. No runaround - just reliable work, and the respect every customer deserves.

What Makes Us Different???

Upfront Fixed Pricing
No surprises, no hidden fees. You get clear, honest quotes before any work begins.

Respectful, Customer-First Service
We show up on time, communicate clearly, and treat your property like it’s our own.

Locals Serving Locals
We’re proud to support the Perth community with reliable, high-quality plumbing backed by real local care.

FOR THE DESIGNER A little background on us as a new biz for your reference:
By Locals, For Locals
After 13 years in the plumbing industry, seasoned local plumber Marcus founded his company to address the widespread issue of homeowners and businesses being overcharged or receiving inferior work. He knew there had to be a better way—and that’s when Quillon was created.
Today, Quillon Group is a trusted plumbing company based in Osborne Park, proudly serving residential, commercial, and industrial clients across the Perth metro area. With over a decade of experience, we deliver expert workmanship, fair pricing, and treat every job—big or small—with the same care and professionalism.
Need it done right—and affordably? Sort it with QUILLON today!

```html
<!DOCTYPE html>
<html lang="en">
<head>
<meta charset="utf-8">
<title>Quillon Plumbing Group – Facebook Banner</title>
<link rel="stylesheet" href="https://fonts.googleapis.com/css2?family=Montserrat:wght@400;500;600&family=Poppins:wght@700;800&display=swap">
<style>
  :root{
    --stage:#25252f;
    --white:#ffffff;
    --navy:#3a3466;
    --navy-text:#2f2e66;
    --deep-blue:#2b5d9b;
    --cyan:#00aeef;
    --cyan-text:#1ba3e6;
    --panel-grey:#d9dbe0;
  }
  *{margin:0;padding:0;box-sizing:border-box}
  html,body{width:1200px;height:668px;overflow:hidden;background:var(--stage)}
  body{position:relative;font-family:"Montserrat",sans-serif}
  .banner{position:absolute;left:72px;top:133px;width:1055px;height:403px;background:var(--white);overflow:hidden}
  .abs{position:absolute}
  .shapes{position:absolute;left:0;top:0}
  .dot-pattern{left:9px;top:9px;width:91px;height:20px;border-radius:4px;
    background:linear-gradient(90deg,rgba(58,52,102,.35),rgba(0,174,239,.25))}
  .brand-name{left:30px;top:42px;width:300px;font-family:"Poppins",sans-serif;font-weight:700;
    font-size:58px;letter-spacing:4px;color:var(--navy);line-height:1}
  .service-area{left:0;top:146px;width:400px;text-align:center;font-family:"Poppins",sans-serif;
    font-weight:800;font-size:21.5px;line-height:27px;color:var(--white)}
  .services-label{left:500px;top:6px;width:476px;text-align:center;font-family:"Poppins",sans-serif;
    font-weight:800;font-size:23px;color:var(--cyan-text);line-height:30px}
  .services-intro{left:470px;top:33px;width:536px;text-align:center;font-family:"Poppins",sans-serif;
    font-weight:800;font-size:22.5px;color:var(--white);line-height:30px;white-space:nowrap}
  .plumbing-box{left:478px;top:65px;width:515px;height:38px;border-radius:5px;
    background:linear-gradient(180deg,#ffffff,var(--panel-grey));
    color:var(--deep-blue);font-size:12.6px;font-weight:500;line-height:17px;text-align:center;padding-top:2px}
  .service-icon{width:49px;height:49px;border-radius:5px;background:linear-gradient(135deg,#3cc3f5,#0a8fd8)}
  .service-title{font-family:"Poppins",sans-serif;font-weight:800;font-size:13px;color:var(--white);line-height:22px}
  .service-desc{font-size:10.4px;color:var(--white);line-height:17px}
  .mission-label{left:7px;top:224px;font-family:"Poppins",sans-serif;font-weight:800;font-size:23px;color:var(--cyan-text)}
  .mission-band{left:158px;top:214px;width:890px;height:49px;border-radius:18px 18px 18px 0;
    background:linear-gradient(90deg,#2d4f8e,#1d7cc5 55%,var(--cyan));
    color:var(--white);font-size:12.4px;line-height:22px;padding:5px 0 0 13px;white-space:nowrap;overflow:hidden}
  .different-title{left:0;top:265px;width:1055px;text-align:center;font-family:"Poppins",sans-serif;
    font-weight:800;font-size:22.5px;color:var(--cyan-text);line-height:32px}
  .point{top:297px;text-align:center;color:var(--navy-text)}
  .point h3{font-family:"Poppins",sans-serif;font-weight:700;font-size:12.5px;line-height:20px}
  .point p{font-size:13px;line-height:18px}
  .contact-bar{left:0;top:356px;width:1055px;height:47px;border-radius:22px 22px 0 0;
    background:linear-gradient(90deg,#3a3568,#2e5f9c)}
  .contact{top:366px;white-space:nowrap;color:var(--white);line-height:28px}
  .contact .label{color:var(--cyan-text);font-size:16px;font-weight:500}
  .contact .value{font-size:25px}
  .contact .phone{font-family:"Poppins",sans-serif;font-weight:800;font-size:24px}
</style>
</head>
<body>
<div class="banner">
  <svg class="shapes" width="1055" height="403" viewBox="0 0 1055 403">
    <defs>
      <linearGradient id="panelFill" x1="0" y1="0" x2="1" y2="0">
        <stop offset="0" stop-color="#3a3466"/>
        <stop offset="1" stop-color="#2c5f9c"/>
      </linearGradient>
      <linearGradient id="areaBand" x1="0" y1="0" x2="1" y2="0">
        <stop offset="0" stop-color="#2c5f9f"/>
        <stop offset="1" stop-color="#00aeef"/>
      </linearGradient>
    </defs>
    <path class="services-panel" fill="url(#panelFill)"
      d="M501,0 H1055 L1025,136 Q1000,213 900,213 H0 V141 H431 L452,50 Q464,0 501,0 Z"/>
    <path class="area-band" fill="url(#areaBand)"
      d="M0,141 H431 Q412,205 360,213 H34 Q0,213 0,180 Z"/>
  </svg>

  <div class="abs dot-pattern" role="img" aria-label="Decorative dot pattern"></div>
  <div class="abs brand-name">QUILLON</div>

  <p class="abs service-area">Servicing: Perth Metro Areas<br>and surrounding suburbs</p>

  <h2 class="abs services-label">Services:</h2>
  <p class="abs services-intro">We offer a wide range of services, including:</p>
  <p class="abs plumbing-box">Plumbing – General maintenance, blocked drains, toilet repairs, burst pipes,<br>reticulation, renovations &amp; emergencies.</p>

  <div class="abs service-icon" style="left:486px;top:116px">
    <svg width="49" height="49" viewBox="0 0 49 49" fill="none" stroke="#fff" stroke-width="2" stroke-linecap="round">
      <path d="M29 10 v18 a6 6 0 1 0 6 0 v-18 a3 3 0 0 0 -6 0z"/>
      <path d="M10 12 q2 3 0 6 M15 12 q2 3 0 6 M20 12 q2 3 0 6"/>
      <path d="M8 26 q4 -3 8 0 t8 0"/>
      <circle cx="12" cy="37" r="2.5"/><circle cx="19" cy="33" r="2"/>
    </svg>
  </div>
  <div class="abs" style="left:541px;top:110px">
    <h3 class="service-title">Hot Water</h3>
    <p class="service-desc" style="margin-top:-1px">Installation, servicing<br>&amp; repairs for<br>all systems.</p>
  </div>

  <div class="abs service-icon" style="left:655px;top:116px">
    <svg width="49" height="49" viewBox="0 0 49 49" fill="none" stroke="#fff" stroke-width="2" stroke-linecap="round">
      <path d="M24.5 9 v31"/>
      <path d="M24.5 12 a12 12 0 0 0 0 25"/>
      <path d="M26 16 l10 -4 M26 24.5 h13 M26 33 l10 4 M32 19 l3 5 -3 5"/>
      <path d="M9 24.5 h4 M12 14 l3 3 M12 35 l3 -3"/>
    </svg>
  </div>
  <div class="abs" style="left:710px;top:111px">
    <h3 class="service-title">Cooling &amp;<br>Heating</h3>
    <p class="service-desc" style="margin-top:1px">Air conditioning,<br>evaporative cooling<br>&amp; heater servicing.</p>
  </div>

  <div class="abs service-icon" style="left:815px;top:116px">
    <svg width="49" height="49" viewBox="0 0 49 49" fill="none" stroke="#fff" stroke-width="2" stroke-linecap="round">
      <path d="M24.5 8 q6 9 6 13 a6 6 0 0 1 -12 0 q0 -4 6 -13z"/>
      <path d="M6 25 l5 4 h27 l5 -4"/>
      <path d="M14 34 q2 3 0 5 M24.5 36 q2 3 0 5 M35 34 q2 3 0 5"/>
    </svg>
  </div>
  <div class="abs" style="left:870px;top:111px">
    <h3 class="service-title">Filtration</h3>
    <p class="service-desc">Filtered taps, under-sink<br>systems &amp; whole-house<br>filtration setups.</p>
  </div>

  <h2 class="abs mission-label">Our Mission</h2>
  <p class="abs mission-band">Quillon Group believes plumbing shouldn't break the bank - or your trust. Our mission is to provide honest, affordable, and no-nonsense<br>plumbing services that get the job done right the first time. No runaround - just reliable work, and the respect every customer deserves.</p>

  <h2 class="abs different-title">What Makes Us Different???</h2>
  <div class="abs point" style="left:29px;width:300px">
    <h3>Upfront Fixed Pricing</h3>
    <p>No surprises, no hidden fees. You get clear,<br>honest quotes before any work begins.</p>
  </div>
  <div class="abs point" style="left:327px;width:310px">
    <h3>Respectful, Customer-First Service</h3>
    <p>We show up on time, communicate clearly,<br>and treat your property like it’s our own.</p>
  </div>
  <div class="abs point" style="left:621px;width:420px">
    <h3>Locals Serving Locals</h3>
    <p>We’re proud to support the Perth community with reliable,<br>high-quality plumbing backed by real local care.</p>
  </div>

  <div class="abs contact-bar"></div>
  <p class="abs contact" style="left:67px"><span class="label">Phone:</span> <span class="phone">0491 726 384</span></p>
  <p class="abs contact" style="left:340px"><span class="label">Email:</span> <span class="value">hello@quillon.com.au</span></p>
  <p class="abs contact" style="left:686px"><span class="label">website:</span> <span class="value">www.quillon.com.au</span></p>
</div>
</body>
</html>
```